Webdesign for silver path

"Der Sternenpfad" is a new info product that will be selled through the website maybe you will create for us.

Translated from german to english the project is named "the silver path". It´s an online video course that teaches people how to live a fulfilling, happy and healthy life.

Design paramaters
We want a serious design that embodies the real feeling of beeing happy and fulfilled. Visitors should even feel good/better when they see the website.
In color psychology some sort of calming deep green like a four-leaf clover is recommend.
Mainly the website will be the external sales page with a big video as the central attention.
We also need a member area for customers to watch our video course.

So mainly we need a eye-cathing, calming header, the content body with mainly video and just a few written words...and of course a footer for links like imprint, affiliate program etc.

What we not want:
- some kind of these exaggerated smiling photos
- that bathetic luck symbols like money or boats
Updates

Hi,

i posted a message to the design discussion. Thank you!

Industry/Entity Type

Affiliate

```html
<!DOCTYPE html>
<html lang="en">
<head>
<meta charset="utf-8">
<title>Der Sternenpfad</title>
<link rel="stylesheet" href="https://fonts.googleapis.com/css2?family=Arimo:wght@400;700&display=swap">
<style>
:root{
  --green-dark:#0b4f0e;
  --green:#1f9a17;
  --green-bright:#26c41c;
  --orange:#f2b01e;
  --orange-light:#ffd466;
  --orange-dark:#d88f05;
  --text:#3a3a3a;
  --grey:#8a8a8a;
  --white:#fff;
}
*{box-sizing:border-box;margin:0;padding:0}
html,body{width:1200px;height:1016px;overflow:hidden;background:var(--white);font-family:"Arimo",Arial,sans-serif;color:var(--text)}
.page{position:relative;width:1200px;height:1016px}
.abs{position:absolute}

/* header */
.brand{left:88px;top:17px;font-size:31px;color:var(--grey);font-weight:400;letter-spacing:.2px}
.field{top:28px;height:26px;border:1px solid #b9b9b9;border-radius:5px;background:linear-gradient(#f0f0f0,#fafafa);font-size:12px;color:#666;padding:6px 9px}
.field.user{left:580px;width:209px}
.field.pass{left:810px;width:209px}
.btn-login{left:1036px;top:27px;width:79px;height:27px;border-radius:5px;border:1px solid #2d5c0e;background:linear-gradient(#6db33a,#3c7d14);color:#fff;font-weight:700;font-size:14px;text-align:center;line-height:25px}

/* nav */
.nav{left:0;top:70px;width:1200px;height:50px;background:linear-gradient(#ffe9a0 0%,var(--orange) 45%,var(--orange-dark) 100%)}
.nav a{position:absolute;top:16px;font-size:14px;font-weight:700;color:#4a3a10;text-decoration:none;transform:translateX(-50%)}
.nav .home{left:89px;top:3px;width:87px;height:47px;background:var(--green-dark);border-radius:5px 5px 0 0;color:#fff;transform:none;text-align:center;line-height:42px}
.search{left:911px;top:10px;width:205px;height:26px;border-radius:5px;background:#fff;font-size:12px;color:#777;padding:7px 12px}
.search svg{position:absolute;right:9px;top:6px}

/* hero */
.hero{left:0;top:120px;width:1200px;height:440px;background:linear-gradient(#0b560c 0%,#1a9c14 35%,#25c11b 62%,#1f8f19 85%,#1d7a1c 100%)}
.deco{left:540px;top:5px;width:230px;height:405px;border-radius:50% 50% 40% 40%;background:radial-gradient(ellipse at 45% 35%,rgba(140,240,110,.55),rgba(40,170,30,.25) 60%,rgba(40,170,30,0) 75%)}
.hero h1{left:89px;top:108px;font-size:31px;font-weight:700;color:#fff}
.hero p{left:90px;width:490px;font-size:12px;line-height:18px;color:#fff}
.hero .p1{top:162px}
.hero .p2{top:234px}
.btn-orange{left:88px;top:315px;width:110px;height:36px;border-radius:5px;background:linear-gradient(#ffd86a,var(--orange) 55%,var(--orange-dark));color:#4a2f00;font-weight:700;font-size:14px;text-align:center;line-height:35px}
.player{left:651px;top:51px;width:465px;height:370px;background:#fff;padding:6px}
.screen{position:relative;width:451px;height:314px;background:radial-gradient(ellipse at 55% 45%,#a79d7c,#776f52 60%,#4f4834)}
.screen .play{position:absolute;left:214px;top:126px}
.controls{position:relative;width:451px;height:44px;background:linear-gradient(#e8e8e8,#c9c9c9);font-size:9px;color:#555}
.controls span{position:absolute}
.bar{left:46px;top:8px;width:362px;height:4px;background:#888;border-radius:2px}
.bar i{display:block;width:243px;height:4px;background:#555}
.knob{left:160px;top:4px;width:20px;height:11px;background:#555;border-radius:4px}
.menu{right:8px;top:24px;border:1px solid #999;padding:1px 5px;background:#eee}

/* content */
.welcome h2{position:absolute;left:88px;top:584px;font-size:24px;font-weight:700;color:#444}
.body-text{left:87px;width:663px;font-size:14px;line-height:18px;text-align:justify;color:#444}
.news{left:785px;top:587px;width:328px;height:319px;border:1px solid #dcdcdc;border-radius:7px;overflow:hidden}
.news h3{height:41px;background:linear-gradient(#ffe39a,var(--orange) 55%,var(--orange-dark));font-size:17px;font-weight:700;color:#3c2c05;padding:10px 27px}
.news p{position:absolute;left:27px;width:277px;font-size:14px;line-height:18px;text-align:justify;color:#444}
.btn-green{left:26px;top:258px;width:110px;height:36px;border-radius:5px;border:1px solid #2a5a0c;background:linear-gradient(#68ab35,#3a7812);color:#fff;font-weight:700;font-size:14px;text-align:center;line-height:33px}

/* footer */
.footer{left:0;top:939px;width:1200px;height:77px;background:linear-gradient(#2a2a2a,#000);text-align:center;font-size:12px;color:#aaa}
.footer .links{position:absolute;top:17px;width:100%}
.footer .copy{position:absolute;top:41px;width:100%}
</style>
</head>
<body>
<div class="page">
  <header>
    <div class="abs brand">Der Sternenpfad</div>
    <div class="abs field user">Username</div>
    <div class="abs field pass">Password</div>
    <div class="abs btn-login">Login</div>
  </header>

  <nav class="abs nav">
    <a class="home" href="#">Home</a>
    <a href="#" style="left:262px">About Us</a>
    <a href="#" style="left:403px">Services</a>
    <a href="#" style="left:546px">Solutions</a>
    <a href="#" style="left:675px">Blog</a>
    <a href="#" style="left:805px">Contact Us</a>
    <div class="abs search">Search
      <svg width="14" height="14" viewBox="0 0 14 14"><circle cx="8" cy="6" r="4" fill="none" stroke="#3a6fb0" stroke-width="1.8"/><line x1="5" y1="9" x2="1.5" y2="12.5" stroke="#3a6fb0" stroke-width="2"/></svg>
    </div>
  </nav>

  <section class="abs hero">
    <div class="abs deco" role="img" aria-label="Glossy green clover leaf illustration"></div>
    <h1 class="abs">Lorem Lipsum Dolor Sit Amet</h1>
    <p class="abs p1">Lorem ipsum dolor sit amet, consectetur adipisicing elit, sed do eiusmod tempor incididunt ut labore et dolore magna aliqua. Ut enim ad minim veniam, quis nostrud exercitation ullamco laboris nisi ut aliquip ex ea commodo consequat.</p>
    <p class="abs p2">Lorem ipsum dolor sit amet, consectetur adipisicing elit, sed do eiusmod tempor incididunt ut labore et dolore magna aliqua. Ut enim ad minim veniam, quis nostrud exercitation ullamco laboris nisi ut aliquip ex ea commodo consequat.</p>
    <div class="abs btn-orange">Read More</div>

    <div class="abs player">
      <div class="screen" role="img" aria-label="Video still: a hand holding soil with a small green seedling">
        <svg class="play" width="42" height="84" viewBox="0 0 42 84"><polygon points="0,0 42,42 0,84" fill="#fff"/></svg>
      </div>
      <div class="controls">
        <span style="left:6px;top:5px">01:46</span>
        <span class="bar"><i></i></span>
        <span class="knob"></span>
        <span style="right:9px;top:5px">02:28</span>
        <span style="left:6px;top:27px"><b style="letter-spacing:2px">❚❚</b>&nbsp; PAUSE</span>
        <span style="left:119px;top:27px">✉ email</span>
        <span style="left:174px;top:27px">⛓ get link</span>
        <span style="left:233px;top:27px">◉ get code</span>
        <span style="left:352px;top:26px">⛶</span>
        <span style="left:378px;top:26px">🔈</span>
        <span class="menu">MENU</span>
      </div>
    </div>
  </section>

  <section class="welcome">
    <h2>Welcome</h2>
    <p class="abs body-text" style="top:631px">Sed ut perspiciatis unde omnis iste natus error sit voluptatem accusantium doloremque laudantium, totam rem aperiam, eaque ipsa quae ab illo inventore veritatis et quasi architecto beatae vitae dicta sunt explicabo. Nemo enim ipsam voluptatem quia voluptas sit aspernatur aut odit aut fugit, sed quia consequuntur magni dolores eos qui ratione voluptatem sequi nesciunt. Neque porro quisquam est, qui dolorem ipsum quia dolor sit amet, consectetur, adipisci velit, sed quia non numquam eius modi tempora incidunt ut labore et dolore magnam aliquam quaerat voluptatem. Ut enim ad minima veniam, quis nostrum exercitationem ullam corporis suscipit laboriosam, nisi ut aliquid ex ea commodi consequatur? Quis autem vel eum iure reprehenderit qui in ea voluptate velit esse quam nihil molestiae consequatur, vel illum qui dolorem eum fugiat quo voluptas nulla pariatur.</p>
    <p class="abs body-text" style="top:811px">Sed ut perspiciatis unde omnis iste natus error sit voluptatem accusantium doloremque laudantium, totam rem aperiam, eaque ipsa quae ab illo inventore veritatis et quasi architecto beatae vitae dicta sunt explicabo. Nemo enim ipsam voluptatem quia voluptas sit aspernatur aut odit aut fugit, sed quia consequuntur magni dolores eos qui ratione voluptatem sequi nesciunt. Neque porro quisquam est, qui dolorem ipsum quia dolor sit amet, consectetur, adipisci velit, sed quia non numquam eius</p>
  </section>

  <aside class="abs news">
    <h3>Latest News</h3>
    <p style="top:63px">Sed ut perspiciatis unde omnis iste natus error sit voluptatem accusantium doloemque laudantium, totam rem aperiam, eaque ipsa quae ab illo inventore.</p>
    <p style="top:163px">Sed ut perspiciatis unde omnis iste natus error sit voluptatem accusantium doloemque laudantium, totam rem aperiam, eaque ipsa quae ab illo inventore.</p>
    <div class="abs btn-green">Read More</div>
  </aside>

  <footer class="abs footer">
    <div class="links">Home &nbsp;|&nbsp; About Us &nbsp;|&nbsp; Services &nbsp;|&nbsp; Solutions &nbsp;|&nbsp; Blog &nbsp;|&nbsp; Contact Us</div>
    <div class="copy">©&nbsp; 2012. All Rights Reserved.</div>
  </footer>
</div>
</body>
</html>
```